Business Card Design

We would like a business card that utilizes our current logo and keeps with the same feel - elegant and organic. Our farm isn't about mass production, it's about excellence, education, beautiful events and flowers - people, culture, and community.

Target Market(s)

Patrons to our farm who are interested in weddings, events, or our flowers and vegetables.

Contact Information for Business Card

Name, address, cell email (Danielle Hoskins, 2716 Wrenfield Rd, Alder Springs, CO 80617, cell 30.412.6638, email danielle@wrenfieldacres.com)

```html
<!DOCTYPE html>
<html lang="en">
<head>
<meta charset="utf-8">
<title>Wrenfield Acres — Business Card</title>
<link href="https://fonts.googleapis.com/css2?family=Arimo:wght@400&family=Cormorant+Garamond:ital,wght@1,500&display=swap" rel="stylesheet">
<style>
  :root {
    --backdrop: #8a7889;
    --sage: #758a76;
    --card-white: #ffffff;
    --ink: #111111;
    --grey-text: #6f6f6f;
    --faint-leaf: #efeef2;
  }
  html, body {
    margin: 0;
    width: 1200px;
    height: 1000px;
    overflow: hidden;
    background: var(--backdrop);
  }
  p, h1 { margin: 0; }
  .canvas {
    position: relative;
    width: 1200px;
    height: 1000px;
  }
  .card {
    position: absolute;
    left: 294px;
    width: 613px;
    height: 351px;
    border-radius: 24px;
    overflow: hidden;
  }
  .card--front {
    top: 118px;
    background: var(--sage);
    color: var(--card-white);
    text-align: center;
  }
  .card--back {
    top: 530px;
    background: var(--card-white);
  }
  .brand-name {
    position: absolute;
    font-family: "Arimo", Arial, sans-serif;
    font-weight: 400;
    letter-spacing: 0.06em;
    line-height: 1;
    white-space: nowrap;
  }
  .card--front .brand-name {
    left: 0;
    top: 160px;
    width: 100%;
    font-size: 40px;
    color: var(--card-white);
  }
  .website {
    position: absolute;
    left: 0;
    top: 290px;
    width: 100%;
    font-family: "Arimo", Arial, sans-serif;
    font-size: 22px;
    line-height: 1;
    color: var(--card-white);
  }
  .card--back .brand-name {
    left: 48px;
    top: 80px;
    font-size: 19px;
    color: var(--sage);
  }
  .leaf-decoration {
    position: absolute;
    left: 440px;
    top: 36px;
    width: 150px;
    height: 315px;
    border-radius: 75px 75px 0 0;
    background: linear-gradient(180deg, var(--faint-leaf), rgba(239,238,242,0.35));
  }
  .contact-line {
    position: absolute;
    left: 46px;
    line-height: 1;
    white-space: nowrap;
  }
  .person-name {
    top: 152px;
    font-family: "Cormorant Garamond", "Times New Roman", serif;
    font-style: italic;
    font-weight: 500;
    font-size: 50px;
    color: var(--ink);
  }
  .email, .phone, .address {
    font-family: "Arimo", Arial, sans-serif;
    color: var(--grey-text);
  }
  .email { top: 205px; left: 44px; font-size: 22px; }
  .phone { top: 253px; font-size: 22px; }
  .address { top: 304px; font-size: 16px; letter-spacing: 0.02em; }
</style>
</head>
<body>
<main class="canvas">
  <section class="card card--front">
    <p class="brand-name">Wrenfield Acres</p>
    <p class="website">wrenfieldacres.com</p>
  </section>

  <section class="card card--back">
    <div class="leaf-decoration" role="img" aria-label="Faint large leaf sprig decoration"></div>
    <p class="brand-name">Wrenfield Acres</p>
    <h1 class="contact-line person-name">Danielle Hoskins</h1>
    <p class="contact-line email">danielle@wrenfieldacres.com</p>
    <p class="contact-line phone">30.412.6638</p>
    <p class="contact-line address">2716 Wrenfield Rd • Alder Springs, CO 80617</p>
  </section>
</main>
</body>
</html>
```